Classy, Elegant, Simple Business Card Design

Looking to have a classy, simple, and elegant design. Want a top notch designed business card. I really like the look of the new brivo credit card. I also like the design I attached. I am trying to reach 21-29 year old females for booking us for there wedding or event. We offer Disc Jockey Service, Photo Booth Rentals, and Uplighting .

Target Market(s)

21-28 year old females

Contact Information for Business Card

Has to have logo, website, email, and phone number

Font styles to use
Other font styles liked:
• open to font choice, modern, clean
Designer to choose
33a6d7
0791cd
0555a3
ffffff

Requirements
Must have
• Has to have logo, website, email, and phone number
Nice to have
• I really like the design of the new brivo credit card. I also included my logo and some designs I like
Should not have
• clutter or too much info

```html
<!DOCTYPE html>
<html lang="en">
<head>
<meta charset="utf-8">
<title>Tidecrest Events – Business Card</title>
<link rel="stylesheet" href="https://fonts.googleapis.com/css2?family=Didact+Gothic&family=Mulish:wght@400;700;800&display=swap">
<style>
  :root {
    --sky: #33a6d7;
    --azure: #0791cd;
    --royal: #0555a3;
    --white: #ffffff;
    --ink: #3a3f47;
    --muted: #6b7077;
    --stage: #e4e5e7;
    --ghost: #eef0f6;
  }
  html, body {
    margin: 0;
    padding: 0;
    width: 1200px;
    height: 1200px;
    overflow: hidden;
    background: var(--stage);
  }
  .canvas {
    position: relative;
    width: 1200px;
    height: 1200px;
  }
  .card {
    position: absolute;
    background: var(--white);
    overflow: hidden;
    box-shadow: 0 2px 6px rgba(0,0,0,0.08);
  }
  .card--front {
    left: 267px; top: 155px; width: 671px; height: 392px;
    display: flex; align-items: center; justify-content: center;
  }
  .front-mark {
    font-family: "Mulish", sans-serif;
    font-weight: 800;
    font-size: 118px;
    letter-spacing: -1px;
    color: var(--azure);
  }
  .card--back {
    left: 266px; top: 662px; width: 668px; height: 391px;
  }
  .ghost-mark {
    position: absolute;
    left: 390px; top: 70px;
    font-family: "Mulish", sans-serif;
    font-weight: 800;
    font-size: 230px;
    line-height: 1;
    color: var(--ghost);
    white-space: nowrap;
  }
  .brand {
    position: absolute;
    left: 48px; top: 112px;
    display: flex; align-items: center; gap: 12px;
    font-family: "Mulish", sans-serif;
    font-weight: 800;
    font-size: 40px;
    color: var(--azure);
  }
  .brand-dot {
    width: 34px; height: 34px; border-radius: 50%;
    background: var(--azure);
  }
  .holder {
    position: absolute;
    left: 48px; top: 200px;
    margin: 0;
    font-family: "Mulish", sans-serif;
    font-size: 25px;
    letter-spacing: 0.5px;
    color: var(--azure);
    font-weight: 400;
  }
  .holder strong { color: var(--royal); font-weight: 800; }
  .rule {
    position: absolute;
    left: 48px; top: 246px;
    width: 574px; height: 2px;
    background: var(--azure);
  }
  .contacts {
    position: absolute;
    left: 48px; top: 262px;
    margin: 0; padding: 0; list-style: none;
    font-family: "Didact Gothic", sans-serif;
    font-size: 18px;
    color: var(--ink);
  }
  .contacts li {
    display: flex; align-items: center;
    height: 26px;
  }
  .contacts svg { width: 26px; height: 20px; margin-right: 6px; flex: none; }
</style>
</head>
<body>
<main class="canvas">
  <section class="card card--front" aria-label="Card front">
    <span class="front-mark">Tidecrest</span>
  </section>

  <section class="card card--back" aria-label="Card back">
    <span class="ghost-mark" aria-hidden="true">Tidecrest</span>

    <div class="brand">
      <span class="brand-dot"></span>
      <span>Tidecrest Events</span>
    </div>

    <h1 class="holder">DANIEL <strong>HARLOW</strong></h1>
    <div class="rule"></div>

    <ul class="contacts">
      <li>
        <svg viewBox="0 0 26 20" aria-hidden="true"><rect x="8" y="1" width="10" height="18" rx="2" fill="none" stroke="var(--azure)" stroke-width="1.8"/><circle cx="13" cy="16" r="1" fill="var(--azure)"/></svg>
        123 456 7890
      </li>
      <li>
        <svg viewBox="0 0 26 20" aria-hidden="true"><rect x="3" y="4" width="20" height="13" fill="var(--azure)"/><path d="M3 4 L13 12 L23 4" fill="none" stroke="var(--white)" stroke-width="1.4"/></svg>
        info@tidecrestevents.com
      </li>
      <li>
        <svg viewBox="0 0 26 20" aria-hidden="true"><circle cx="13" cy="10" r="8.5" fill="none" stroke="var(--azure)" stroke-width="1.6"/><ellipse cx="13" cy="10" rx="3.5" ry="8.5" fill="none" stroke="var(--azure)" stroke-width="1.2"/><path d="M4.5 10 H21.5" stroke="var(--azure)" stroke-width="1.2"/></svg>
        www.tidecrestevents.com
      </li>
      <li>
        <svg viewBox="0 0 26 20" aria-hidden="true"><path d="M13 19 C8 12 6 10 6 7 A7 7 0 0 1 20 7 C20 10 18 12 13 19 Z" fill="var(--azure)"/><circle cx="13" cy="7" r="2.5" fill="var(--white)"/></svg>
        Suit 123, City, Country, Postal Code
      </li>
    </ul>
  </section>
</main>
</body>
</html>
```